Design WORDPRESS Website for E Commerce Business

We are needing a WORDPRESS website for an E Commerce Business that is supplying quailty kids / baby products.

Target Market(s)

Female / Working Mums / New Mums

Industry/Entity Type

Business

Number of Pages Required

1 page

Font styles to use
Sans Serif

Colors
33b8a4
f8fcfd
d3a5cc
f7f1f7
cbcbcb
9d9d9d

```html
<!DOCTYPE html>
<html lang="en">
<head>
<meta charset="utf-8">
<title>Tot &amp; Tumble</title>
<link href="https://fonts.googleapis.com/css2?family=Montserrat:wght@400;500;600;700&family=Dancing+Script:wght@500&display=swap" rel="stylesheet">
<style>
:root{
  --red:#e5373f;
  --teal:#5ec4b5;
  --teal-dark:#33b8a4;
  --pink-line:#ee7478;
  --ink:#222;
  --rule:#cbcbcb;
  --white:#fff;
}
*{margin:0;padding:0;box-sizing:border-box}
html,body{width:1200px;height:1200px;overflow:hidden;background:var(--white);font-family:'Montserrat',sans-serif;color:var(--ink)}
.page{position:relative;width:1200px;height:1200px}
.top-accent{position:absolute;left:0;top:0;width:1200px;height:3px;background:var(--teal)}
.utility{position:absolute;left:120px;top:12px;width:960px;display:flex;justify-content:space-between;font-size:9.5px}
.utility nav{display:flex;gap:14px;color:var(--red);font-weight:600}
.utility nav span.dot{font-weight:700}
.utility-rule{position:absolute;left:120px;top:34px;width:960px;height:1px;background:#ddd}
.brand{position:absolute;left:120px;top:58px;display:flex;align-items:center;gap:8px;color:var(--teal);font-weight:500;font-size:30px;line-height:28px}
.brand-mark{width:40px;height:40px;border-radius:50%;background:#8a8a8a}
.social{position:absolute;left:418px;top:70px;display:flex;gap:19px}
.social span{width:27px;height:27px;border-radius:50%;background:#f6b8bb}
.social span.active{background:var(--red)}
.search{position:absolute;left:689px;top:65px;width:390px;height:42px;border:2px solid var(--red);border-radius:8px;display:flex;overflow:hidden}
.search input{flex:1;border:0;padding-left:12px;font:500 11px 'Montserrat',sans-serif;color:#555;background:none}
.search button{width:41px;background:var(--red);border:0;display:flex;align-items:center;justify-content:center}
.mainnav{position:absolute;left:0;top:134px;width:1200px;height:56px;background:var(--red)}
.mainnav ul{list-style:none;display:flex;justify-content:space-between;width:960px;margin:0 auto;height:100%;align-items:center}
.mainnav li{color:var(--white);font-weight:600;font-size:11.5px;padding:0 22px;border-left:1px dashed rgba(255,255,255,.9);line-height:34px}
.mainnav li:first-child{border:0;padding-left:0}
.mainnav li:last-child{padding-right:0}
.hero{position:absolute;left:121px;top:189px;width:959px;height:425px;background:radial-gradient(circle at 30% 30%,#e8cdb5,#c99a86 45%,#a57a6a 80%)}
.hero-panel{position:absolute;left:605px;top:0;width:279px;height:423px;background:rgba(70,50,45,.72);color:var(--white);text-align:center}
.hero-panel h2{margin-top:71px;font-size:21px;font-weight:700}
.hero-panel h3{font-size:32px;font-weight:700;margin-top:4px}
.hero-panel p{font-size:11.5px;font-weight:600;line-height:19px;margin:28px 18px 0}
.cta{display:inline-block;margin-top:50px;background:var(--red);color:var(--white);font-weight:700;font-size:12.5px;padding:14px 26px;border-radius:2px}
.welcome{position:absolute;left:0;top:650px;width:1200px;text-align:center;font-family:'Dancing Script',cursive;font-size:33px;color:var(--red)}
.features{position:absolute;left:0;top:736px;width:1200px}
.feature{position:absolute;width:220px;text-align:center}
.feature .ring{width:160px;height:160px;border:1.5px solid var(--pink-line);border-radius:50%;margin:0 auto;display:flex;align-items:center;justify-content:center}
.feature h4{margin-top:34px;font-weight:500;font-size:19.5px;color:var(--teal)}
.card{position:absolute;top:1016px;width:304px;height:184px;border-radius:6px 6px 0 0}
</style>
</head>
<body>
<div class="page">
  <div class="top-accent"></div>
  <div class="utility">
    <span>Lorem ipsum dolor sit amet, consectetur adipiscing elit posuere lorem</span>
    <nav><span>My Account</span><span class="dot">·</span><span>Need Help?</span><span class="dot">·</span><span>Contact</span><span class="dot">·</span><span>My Savings</span><span class="dot">·</span><span>My Cart</span></nav>
  </div>
  <div class="utility-rule"></div>

  <div class="brand"><span class="brand-mark"></span><span>TOT &amp;<br>TUMBLE</span></div>

  <div class="social" aria-label="Social links">
    <span class="active"></span><span></span><span></span><span></span><span></span>
  </div>

  <form class="search">
    <input type="text" placeholder="SEARCH HERE" value="SEARCH HERE">
    <button type="button" aria-label="Search">
      <svg width="22" height="22" viewBox="0 0 22 22" fill="none" stroke="#fff" stroke-width="1.6"><circle cx="9.5" cy="9.5" r="7.5"/><line x1="15" y1="15" x2="21" y2="21"/></svg>
    </button>
  </form>

  <nav class="mainnav">
    <ul><li>HOME</li><li>WHAT'S NEW</li><li>LOREM</li><li>VIVAMUS</li><li>POSUERE</li><li>ULTRICIES</li><li>SAGITTIS</li><li>CONSECTETUR</li><li>CURSUS</li><li>SSAPIEN</li></ul>
  </nav>

  <section class="hero" role="img" aria-label="Blurred shop interior with warm bokeh lights">
    <div class="hero-panel">
      <h2>BACK TO SCHOOL</h2>
      <h3>SALE!</h3>
      <p>Lorem ipsum dolor sit amet, cosectetur adipiscing elit. Supendisse lobortis congue elit, vitae blandit tortor cursus sodales lorem vel nulla.</p>
      <span class="cta">CLICK HERE</span>
    </div>
  </section>

  <h1 class="welcome">Welcome to Tot &amp; Tumble</h1>

  <section class="features">
    <div class="feature" style="left:91px">
      <div class="ring">
        <svg width="76" height="76" viewBox="0 0 76 76"><path fill="#5ec4b5" d="M38 2l7 6 9-2 3 9 9 3-2 9 6 7-6 7 2 9-9 3-3 9-9-2-7 6-7-6-9 2-3-9-9-3 2-9-6-7 6-7-2-9 9-3 3-9 9 2z"/><g stroke="#fff" stroke-width="4" fill="none"><circle cx="29" cy="29" r="5"/><circle cx="47" cy="47" r="5"/><line x1="49" y1="25" x2="27" y2="51"/></g></svg>
      </div>
      <h4>Big Discounts</h4>
    </div>
    <div class="feature" style="left:356px">
      <div class="ring">
        <svg width="106" height="60" viewBox="0 0 106 60" fill="none" stroke="#5ec4b5" stroke-width="4.5" stroke-linecap="round" stroke-linejoin="round"><path d="M22 8h54v42H60"/><path d="M76 18h16l10 14v18h-8"/><circle cx="40" cy="52" r="5"/><circle cx="88" cy="52" r="5"/><line x1="20" y1="50" x2="35" y2="50"/><line x1="2" y1="26" x2="50" y2="26"/><polyline points="42,18 50,26 42,34"/><line x1="12" y1="36" x2="34" y2="36"/><line x1="14" y1="16" x2="34" y2="16"/></svg>
      </div>
      <h4>Fast Shipping</h4>
    </div>
    <div class="feature" style="left:622px">
      <div class="ring">
        <svg width="88" height="88" viewBox="0 0 88 88" fill="none" stroke="#5ec4b5" stroke-width="3"><circle cx="44" cy="44" r="30"/><ellipse cx="44" cy="44" rx="13" ry="30"/><line x1="44" y1="14" x2="44" y2="74"/><line x1="14" y1="44" x2="74" y2="44"/><path d="M19 30h50M19 58h50"/><path d="M10 34a36 36 0 0 1 56-22M78 54a36 36 0 0 1-56 22" stroke-width="3.5"/></svg>
      </div>
      <h4>Worldwide</h4>
    </div>
    <div class="feature" style="left:888px">
      <div class="ring">
        <svg width="80" height="80" viewBox="0 0 80 80" fill="none" stroke="#5ec4b5" stroke-width="3.5" stroke-linejoin="round" stroke-linecap="round"><path d="M40 4c12 6 22 8 36 8 0 30-10 52-36 64C14 64 4 42 4 12c14 0 24-2 36-8z"/><polyline points="26,40 36,50 54,30" stroke="#9d9d9d"/></svg>
      </div>
      <h4>Secure Shopping</h4>
    </div>
  </section>

  <div class="card" style="left:118px;background:linear-gradient(120deg,#ef1f77 45%,#12bcd6 46%,#fdfdfd 85%)" role="img" aria-label="Pink and teal notebooks with a pen"></div>
  <div class="card" style="left:447px;background:linear-gradient(110deg,#e8c9b4 35%,#f2f4f5 55%,#9ad0e0)" role="img" aria-label="Baby playing with colourful toys"></div>
  <div class="card" style="left:776px;background:linear-gradient(180deg,#5c463f,#2f5a78 70%,#3d6f92)" role="img" aria-label="Two yellow toy figures on a blue background"></div>
</div>
</body>
</html>
```